Business Card with Logo and Company Name.

I would like a business card design that has both my logo and company name. The K7 logo was one part- now I would like the entire Company Name.

KESTRO CONTRACTING SERVICES

I have consulted with my team and we have went over several ideas for the last few weeks. We all love the K7 logo. Great for branding. What we have thought of in regards to the company name to tie into it is giving focus to font selection. We love the idea of KESTRO being a larger font and maybe making CONTRACTING SERVICES a larger font. Much like one would for a Slogan Line and font when designing.

I hope I’m communicating this correctly and not causing confusion. If need be I can mock up or sketch an idea and send. Just let me know.

**** I just noticed an area to upload an image. I uploaded one that was used as an idea*****

```html
<!DOCTYPE html>
<html lang="en">
<head>
<meta charset="utf-8">
<title>Kestro Contracting Services – Business Card</title>
<link href="https://fonts.googleapis.com/css2?family=Karla:wght@400;500;700&display=swap" rel="stylesheet">
<style>
  :root {
    --backdrop: #1d1d1f;
    --card: #a54b25;
    --ink: #ffffff;
    --ink-soft: rgba(255,255,255,0.85);
    --logo: #d8d8d8;
    --rule: rgba(255,255,255,0.7);
  }
  * { margin: 0; padding: 0; box-sizing: border-box; }
  html, body {
    width: 1200px; height: 874px; overflow: hidden;
    background: var(--backdrop);
    font-family: "Karla", Arial, sans-serif;
  }
  .canvas {
    position: relative; width: 1200px; height: 874px;
    display: flex; flex-direction: column; align-items: center; justify-content: center; gap: 36px;
  }
  .card {
    position: relative; width: 640px; height: 366px;
    background: var(--card); border-radius: 22px;
    color: var(--ink);
  }
  .card-front { display: flex; align-items: center; justify-content: center; }
  .brand { text-align: center; color: var(--logo); font-weight: 400; }
  .brand-name { font-size: 86px; letter-spacing: 6px; line-height: 1; }
  .brand-tagline { font-size: 20px; letter-spacing: 4px; margin-top: 4px; }

  .card-back { display: flex; align-items: center; }
  .identity {
    width: 340px; text-align: right; padding-right: 26px; margin-top: 20px;
  }
  .person-name { font-size: 26px; font-weight: 700; letter-spacing: 1px; line-height: 1.1; }
  .person-role { font-size: 16px; color: var(--ink-soft); margin-top: 2px; }
  .divider { width: 1px; height: 120px; background: var(--rule); margin-top: 20px; }
  .contact { list-style: none; padding-left: 24px; margin-top: 20px; font-size: 16px; line-height: 1.35; }
  .contact li { display: flex; align-items: flex-start; gap: 8px; }
  .contact svg { width: 13px; height: 13px; margin-top: 3px; flex: none; fill: var(--ink); }
</style>
</head>
<body>
<main class="canvas">
  <section class="card card-front">
    <div class="brand">
      <div class="brand-name">KESTRO</div>
      <div class="brand-tagline">Contracting Services</div>
    </div>
  </section>

  <section class="card card-back">
    <div class="identity">
      <div class="person-name">DANIEL REYES</div>
      <div class="person-role">President</div>
    </div>
    <div class="divider"></div>
    <ul class="contact">
      <li>
        <svg viewBox="0 0 12 12"><path d="M6 0a4 4 0 0 0-4 4c0 3 4 8 4 8s4-5 4-8a4 4 0 0 0-4-4zm0 5.6A1.6 1.6 0 1 1 6 2.4a1.6 1.6 0 0 1 0 3.2z"/></svg>
        <span>4120 Birchwood Court<br>Juneau, Alaska 99801</span>
      </li>
      <li>
        <svg viewBox="0 0 12 12"><path d="M2.4 0.5l2 2.2-1 1.5c.8 1.7 2.2 3.1 3.9 3.9l1.5-1 2.2 2-1 2.3C5 11 1 7 .5 1.5z"/></svg>
        <span>555-204-7718</span>
      </li>
      <li>
        <svg viewBox="0 0 12 12"><path d="M0 2h12v1L6 7 0 3zM0 4.2l6 4 6-4V10H0z"/></svg>
        <span>info@kestro.com</span>
      </li>
      <li>
        <svg viewBox="0 0 12 12"><circle cx="6" cy="6" r="5.5"/><path d="M.8 6h10.4M6 .5c-2 2.5-2 8.5 0 11M6 .5c2 2.5 2 8.5 0 11" stroke="#a54b25" stroke-width="1" fill="none"/></svg>
        <span>www.kestro.com</span>
      </li>
    </ul>
  </section>
</main>
</body>
</html>
```